Ledgrix Business Card

We need a business card design using the attached logo. The company is a financial services company that provides a dashboard (chart based information) for Executives of small businesses to use to better manage their information. The design must be progressive, make good utilization of the logo and project stability and financial security.

Industry/Entity Type

Financial

```html
<!DOCTYPE html>
<html lang="en">
<head>
<meta charset="utf-8">
<title>Ledgrix Business Card</title>
<link rel="stylesheet" href="https://fonts.googleapis.com/css2?family=Open+Sans:wght@400;700&display=swap">
<style>
  :root {
    --page-bg: #e9e7e4;
    --card-bg: #ffffff;
    --brand-red: #9e1b21;
    --ink: #141414;
    --text: #333333;
    --faint: #f1f0ef;
    --shadow: rgba(0, 0, 0, 0.18);
  }
  * { box-sizing: border-box; margin: 0; padding: 0; }
  html, body {
    width: 1200px;
    height: 471px;
    overflow: hidden;
    background: var(--page-bg);
    font-family: "Open Sans", Arial, sans-serif;
  }
  .stage {
    width: 1200px;
    height: 471px;
    display: flex;
    align-items: center;
    justify-content: center;
    gap: 60px;
  }
  .card {
    position: relative;
    width: 520px;
    height: 300px;
    background: var(--card-bg);
    box-shadow: 0 6px 18px var(--shadow);
    overflow: hidden;
  }

  /* Front */
  .card-front .brand {
    position: absolute;
    left: 26px;
    top: 30px;
    display: flex;
    align-items: center;
    gap: 8px;
  }
  .brand-square {
    width: 30px;
    height: 30px;
    background: var(--brand-red);
  }
  .brand-name {
    font-weight: 700;
    font-size: 32px;
    letter-spacing: -0.5px;
    color: var(--ink);
    line-height: 1;
  }
  .decor-panel {
    position: absolute;
    left: 232px;
    top: 30px;
    width: 250px;
    height: 240px;
    background: var(--faint);
    border-radius: 10px;
  }
  .identity {
    position: absolute;
    left: 300px;
    top: 36px;
  }
  .person-name {
    font-weight: 700;
    font-size: 19px;
    color: var(--brand-red);
    line-height: 1.2;
  }
  .person-title {
    font-size: 14px;
    color: var(--ink);
    margin-top: 2px;
  }
  .contact-block {
    position: absolute;
    left: 36px;
    top: 170px;
    font-size: 14px;
    color: var(--text);
  }
  .contacts {
    list-style: none;
  }
  .contacts li {
    display: flex;
    align-items: center;
    gap: 5px;
    line-height: 22px;
  }
  .contacts svg { width: 12px; height: 12px; flex: none; }
  .address {
    margin-top: 12px;
    padding-left: 14px;
    line-height: 20px;
  }

  /* Back */
  .card-back {
    display: flex;
    align-items: center;
    justify-content: center;
  }
  .card-back .brand {
    display: flex;
    align-items: center;
    gap: 18px;
  }
  .card-back .brand-square { width: 70px; height: 70px; }
  .card-back .brand-name { font-size: 76px; letter-spacing: -1.5px; }
</style>
</head>
<body>
  <main class="stage">
    <section class="card card-front" aria-label="Business card front">
      <div class="decor-panel" aria-hidden="true"></div>
      <div class="brand">
        <span class="brand-square" aria-hidden="true"></span>
        <span class="brand-name">Ledgrix</span>
      </div>
      <div class="identity">
        <p class="person-name">Your Name</p>
        <p class="person-title">Designation</p>
      </div>
      <div class="contact-block">
        <ul class="contacts">
          <li>
            <svg viewBox="0 0 12 12" aria-hidden="true"><circle cx="6" cy="6" r="5.3" fill="none" stroke="#333" stroke-width="1"/><path d="M4 3.2 L5.2 4.6 L4.6 5.3 Q5.4 6.8 6.7 7.4 L7.4 6.8 L8.8 8 L8 8.9 Q5 8.6 3.2 4.2 Z" fill="#333"/></svg>
            123-456-7890
          </li>
          <li>
            <svg viewBox="0 0 12 12" aria-hidden="true"><rect x="1" y="3" width="10" height="7" rx="1" fill="#333"/><path d="M1.5 3.5 L6 7 L10.5 3.5" fill="none" stroke="#fff" stroke-width="1"/></svg>
            hello@ledgrix.com
          </li>
          <li>
            <svg viewBox="0 0 12 12" aria-hidden="true"><circle cx="6" cy="6" r="5" fill="#333"/><path d="M1 6 H11 M6 1 V11 M6 1 Q3 6 6 11 M6 1 Q9 6 6 11" fill="none" stroke="#fff" stroke-width="0.7"/></svg>
            www.ledgrix.com
          </li>
        </ul>
        <p class="address">Street Name City Name<br>State Zipcode</p>
      </div>
    </section>

    <section class="card card-back" aria-label="Business card back">
      <div class="brand">
        <span class="brand-square" aria-hidden="true"></span>
        <span class="brand-name">Ledgrix</span>
      </div>
    </section>
  </main>
</body>
</html>
```